Larchmere Valley College

We are looking to update our current webpage at www.larchmerevalley.ca. We would like to make it modern, fresh and appealing to students. We want to keep our logo the same with the logo colours blended in as the primary colours and focus. We are open to reconfiguring content as well.
Reason: Hi, In the next 3 days we will have narrowed our search to 3 designs and will make a choice before the final deadline...
Industry/Entity Type
College

```html
<!DOCTYPE html>
<html lang="en">
<head>
<meta charset="utf-8">
<title>Larchmere Valley College</title>
<link rel="stylesheet" href="https://fonts.googleapis.com/css2?family=Open+Sans:ital,wght@0,400;0,600;0,700;1,400&family=Nunito:wght@600;700&display=swap">
<style>
:root{
  --teal:#0f6b63;
  --teal-dark:#0b544e;
  --teal-light:#1f8478;
  --navy:#1f2f6b;
  --red:#d23b33;
  --ink:#333;
  --muted:#555;
  --band:#e8e8e8;
  --footer:#3a3a3a;
  --footer-bottom:#2f2f2f;
  --line:#dcdcdc;
}
*{margin:0;padding:0;box-sizing:border-box}
html,body{width:1200px;height:2384px;overflow:hidden;background:#fff}
body{position:relative;font-family:"Open Sans",Arial,sans-serif;color:var(--ink)}
.abs{position:absolute}

/* header */
.brand{left:172px;top:26px;display:flex;align-items:center;gap:12px}
.brand-dot{width:22px;height:22px;border-radius:50%;background:var(--teal)}
.brand-name{font-weight:700;color:var(--teal);font-size:25px;line-height:25px;letter-spacing:.5px;text-transform:uppercase}
.call{left:858px;top:26px;width:170px;text-align:right;font-size:12.5px;color:#666}
.call b{color:#444;font-weight:600}
.call svg{vertical-align:-2px;margin-right:4px}
.tagline{left:640px;top:62px;width:388px;text-align:right;font-family:"Open Sans",Arial,sans-serif;font-size:26px;font-weight:400;letter-spacing:.5px;color:var(--navy)}

/* nav */
.nav{left:0;top:129px;width:1200px;height:49px;background:linear-gradient(#1b7d73,#0e5d56)}
.nav ul{list-style:none;display:flex;margin-left:172px;height:49px}
.nav li{font-size:11.5px;font-weight:600;color:#fff;padding:0 13px;line-height:49px;white-space:nowrap;border-right:1px solid rgba(255,255,255,.12)}
.nav li.active{background:#1a1a1a}

/* hero */
.hero{left:0;top:178px;width:1200px;height:521px;background:linear-gradient(90deg,#d9dde0 0%,#eef0f1 35%,#c6d3d5 55%,#e4e7e8 80%,#d7dcde 100%)}
.hero-caption{left:172px;top:357px;width:330px;height:99px;background:rgba(255,255,255,.82);padding:12px 10px}
.hero-caption h1{font-family:"Nunito",sans-serif;font-weight:700;font-size:35px;line-height:44px;color:var(--teal);white-space:nowrap}
.hero-caption p{font-size:11px;line-height:18px;color:#333;font-weight:600}
.hero-arrow{top:418px;width:51px;height:40px;background:rgba(90,90,90,.75);display:flex;align-items:center;justify-content:center}

/* headings */
.section-title{font-size:23px;font-weight:400;color:#444;font-family:Arial,"Open Sans",sans-serif}

/* campus */
.card{width:261px}
.card .photo{height:180px}
.card h3{margin-top:26px;font-size:14px;font-weight:700;color:var(--teal)}
.card p{margin-top:12px;font-size:11.5px;line-height:20px;color:var(--muted)}
.card .more{margin-top:14px;font-size:13px;font-weight:700;color:var(--red);display:flex;align-items:center;gap:6px}

/* video */
.video{left:172px;top:1171px;width:379px;height:218px;background:linear-gradient(160deg,#6e8a5e,#a9b9c2 55%,#3e4a58)}
.play{left:168px;top:86px;width:48px;height:44px;border-radius:8px;background:#b5201c;display:flex;align-items:center;justify-content:center}
.video-bar{left:0;bottom:0;width:379px;height:20px;background:#1b1b1b}
.feature{left:588px;top:1168px;width:440px}
.feature h2{font-size:23px;font-weight:400;color:#444;font-family:Arial,sans-serif}
.feature p{margin-top:22px;font-size:11.5px;line-height:20px;color:var(--muted)}
.btn{left:588px;top:1349px;width:135px;height:38px;background:var(--navy);color:#fff;font-size:12.5px;border-radius:3px;display:flex;align-items:center;justify-content:center}

/* admissions */
.admissions{left:0;top:1433px;width:1200px;height:285px;background:var(--band)}
.adm-item{top:1510px;width:200px;text-align:center}
.adm-icon{margin:0 auto;width:98px;height:98px;border-radius:50%;border:2px solid var(--teal);padding:4px}
.adm-icon div{width:100%;height:100%;border-radius:50%;background:var(--teal);display:flex;align-items:center;justify-content:center}
.adm-item h4{margin-top:16px;font-size:13.5px;font-weight:600;color:#333}
.adm-item p{margin-top:8px;font-size:11px;line-height:19px;color:var(--muted)}

/* news */
.news{left:172px;width:410px;height:130px;border:1px solid var(--line);background:#fff}
.news .thumb{position:absolute;left:13px;top:14px;width:153px;height:100px;background:linear-gradient(135deg,#7d6a55,#c8b9a4 60%,#5d4e40)}
.news h5{position:absolute;left:189px;top:10px;font-size:14px;font-weight:400;color:#333}
.news p{position:absolute;left:189px;top:44px;width:205px;font-size:11.5px;line-height:20px;color:var(--muted)}
.news .date{position:absolute;left:189px;top:96px;font-size:11.5px;font-weight:700;color:var(--red)}
.map{left:618px;top:1802px;width:410px;height:284px;background:linear-gradient(135deg,#dfe8d4,#eceee6 50%,#dde6d3)}

/* footer */
.footer{left:0;top:2124px;width:1200px;height:176px;background:var(--footer)}
.foot-col{top:2146px;color:#fff}
.foot-col h6{font-size:12.5px;font-weight:700;letter-spacing:.3px;padding-bottom:14px;border-bottom:1px solid #555}
.foot-about p{margin-top:14px;font-size:11px;line-height:20px;color:#eee}
.post{margin-top:14px;display:flex;gap:22px}
.post .thumb{width:103px;height:78px;background:linear-gradient(135deg,#6c6c74,#b6aea2 60%,#4e5058)}
.post b{display:block;font-size:12px;font-weight:400;margin-top:4px}
.post span{display:block;font-size:11.5px;font-weight:700;color:var(--red)}
.social{margin-top:12px;display:grid;grid-template-columns:160px 100px;row-gap:22px}
.social div{display:flex;align-items:center;gap:10px;font-size:12px}
.social i{width:18px;height:18px;border-radius:50%;background:#8a8a8a;display:block}
.bottom{left:0;top:2300px;width:1200px;height:84px;background:var(--footer-bottom);border-top:1px solid #4a4a4a}
.bottom span{position:absolute;top:28px;font-size:11px;color:#fff}
</style>
</head>
<body>

<header>
  <div class="abs brand">
    <span class="brand-dot"></span>
    <div class="brand-name">Larchmere<br>Valley<br>College</div>
  </div>
  <div class="abs call">
    <svg width="13" height="13" viewBox="0 0 24 24"><path fill="#666" d="M6.6 10.8a15.1 15.1 0 0 0 6.6 6.6l2.2-2.2a1 1 0 0 1 1-.25 11.4 11.4 0 0 0 3.6.57 1 1 0 0 1 1 1V20a1 1 0 0 1-1 1A17 17 0 0 1 3 4a1 1 0 0 1 1-1h3.5a1 1 0 0 1 1 1c0 1.25.2 2.450.57 3.57a1 1 0 0 1-.25 1z"/></svg>Call Us : <b>(604) 555-0148</b>
  </div>
  <div class="abs tagline">learn. grow. belong</div>
</header>

<nav class="abs nav">
  <ul>
    <li class="active">Home</li><li>About Us</li><li>Contact Us</li><li>Consider Larchmere</li><li>Current Students</li><li>Alumni</li><li>Supporters</li><li>News + Events</li><li>Larchmere Park</li>
  </ul>
</nav>

<section class="abs hero" role="img" aria-label="Student studying with open books in a bright campus library"></section>
<div class="abs hero-caption">
  <h1>Courses &amp; Events</h1>
  <p>Long established fact that a reader will be distracted By the readable content</p>
</div>
<div class="abs hero-arrow" style="left:0"><svg width="16" height="22" viewBox="0 0 16 22"><path d="M12 2 3 11l9 9" stroke="#fff" stroke-width="3" fill="none"/></svg></div>
<div class="abs hero-arrow" style="left:1149px"><svg width="16" height="22" viewBox="0 0 16 22"><path d="m4 2 9 9-9 9" stroke="#fff" stroke-width="3" fill="none"/></svg></div>

<h2 class="abs section-title" style="left:0;width:1200px;text-align:center;top:732px">Our Campus</h2>

<article class="abs card" style="left:172px;top:791px">
  <div class="photo" role="img" aria-label="Campus building with lawn and trees" style="background:linear-gradient(#8fb7e4 0%,#b9d3ee 45%,#7a7164 60%,#6d8a4f 100%)"></div>
  <h3>Embarrassing Hidden</h3>
  <p>Randomised words which don't look even slightly believable. If you are going to use a passage of Lorem Ipsum, you anything</p>
  <div class="more">MORE <svg width="13" height="13" viewBox="0 0 14 14"><circle cx="7" cy="7" r="6" fill="none" stroke="#d23b33" stroke-width="1.4"/><path d="m6 4 3 3-3 3" fill="none" stroke="#d23b33" stroke-width="1.4"/></svg></div>
</article>
<article class="abs card" style="left:469px;top:791px">
  <div class="photo" role="img" aria-label="Lecturer speaking to a class" style="background:linear-gradient(135deg,#e9e4dc,#9b8b7a 55%,#3c3530)"></div>
  <h3>Predefined Chunks</h3>
  <p>Randomised words which don't look even slightly believable. If you are going to use a passage of Lorem Ipsum, you anything</p>
  <div class="more">MORE <svg width="13" height="13" viewBox="0 0 14 14"><circle cx="7" cy="7" r="6" fill="none" stroke="#d23b33" stroke-width="1.4"/><path d="m6 4 3 3-3 3" fill="none" stroke="#d23b33" stroke-width="1.4"/></svg></div>
</article>
<article class="abs card" style="left:767px;top:791px">
  <div class="photo" role="img" aria-label="Campus bookstore entrance" style="background:linear-gradient(135deg,#d8d3cc,#b9855a 50%,#8a5a36)"></div>
  <h3>Suffered Alteration</h3>
  <p>Randomised words which don't look even slightly believable. If you are going to use a passage of Lorem Ipsum, you anything</p>
  <div class="more">MORE <svg width="13" height="13" viewBox="0 0 14 14"><circle cx="7" cy="7" r="6" fill="none" stroke="#d23b33" stroke-width="1.4"/><path d="m6 4 3 3-3 3" fill="none" stroke="#d23b33" stroke-width="1.4"/></svg></div>
</article>

<div class="abs video" role="img" aria-label="Video of a program instructor speaking outdoors">
  <div class="abs play"><svg width="18" height="20" viewBox="0 0 18 20"><path d="M2 1v18l15-9z" fill="#fff"/></svg></div>
  <div class="abs video-bar"></div>
</div>
<div class="abs feature">
  <h2>Omega Global Destination</h2>
  <p>Larchmere Valley College is pleased to offer a one year program that is geared towards eaddition to music, audio, media and song writing courses, the student will study Bible andspiritual formation issues. "Hands on" application in the recording lab as well as in chapel services will provide experience in areas of interest. Some elective taking private music lessons</p>
</div>
<div class="abs btn">Click View</div>

<section class="abs admissions"></section>
<h2 class="abs section-title" style="left:0;width:1200px;text-align:center;top:1450px">Admissions</h2>

<div class="abs adm-item" style="left:162px">
  <div class="adm-icon"><div><svg width="40" height="30" viewBox="0 0 40 30"><path d="M20 2 1 11l19 9 19-9z" fill="#fff"/><path d="M9 16v7c6 5 16 5 22 0v-7l-11 5z" fill="#fff"/><path d="M36 12v10" stroke="#fff" stroke-width="2"/></svg></div></div>
  <h4>Apply Today</h4>
  <p>There are many variations ofsages of Lorem Ipsum available</p>
</div>
<div class="abs adm-item" style="left:386px">
  <div class="adm-icon"><div><svg width="36" height="32" viewBox="0 0 36 32"><rect x="3" y="3" width="30" height="7" rx="1" fill="#fff"/><rect x="1" y="12" width="34" height="7" rx="1" fill="#fff"/><rect x="3" y="21" width="30" height="7" rx="1" fill="#fff"/><path d="M6 6.5h20M4 15.5h24M6 24.5h20" stroke="#0f6b63" stroke-width="1.2"/></svg></div></div>
  <h4>Admissions Information</h4>
  <p>There are many variations ofsages of Lorem Ipsum available</p>
</div>
<div class="abs adm-item" style="left:609px">
  <div class="adm-icon"><div><svg width="32" height="32" viewBox="0 0 32 32"><rect x="2" y="5" width="28" height="25" rx="2" fill="#fff"/><rect x="2" y="5" width="28" height="6" fill="#dcecea"/><path d="M9 2v6M23 2v6" stroke="#fff" stroke-width="3"/><g fill="#0f6b63"><rect x="6" y="14" width="4" height="3"/><rect x="12" y="14" width="4" height="3"/><rect x="18" y="14" width="4" height="3"/><rect x="24" y="14" width="3" height="3"/><rect x="6" y="19" width="4" height="3"/><rect x="12" y="19" width="4" height="3"/><rect x="18" y="19" width="4" height="3"/><rect x="24" y="19" width="3" height="3"/><rect x="6" y="24" width="4" height="3"/><rect x="12" y="24" width="4" height="3"/></g></svg></div></div>
  <h4>Browse our Programs</h4>
  <p>There are many variations ofsages of Lorem Ipsum available</p>
</div>
<div class="abs adm-item" style="left:833px">
  <div class="adm-icon"><div><svg width="30" height="32" viewBox="0 0 30 32"><path d="M11 2h8v12h6L15 24 5 14h6z" fill="#fff"/><rect x="2" y="27" width="26" height="4" fill="#fff"/></svg></div></div>
  <h4>Download Forms</h4>
  <p>There are many variations ofsages of Lorem Ipsum available</p>
</div>

<h2 class="abs section-title" style="left:172px;top:1750px">News &amp; Events</h2>
<h2 class="abs section-title" style="left:618px;top:1750px">Our Location</h2>

<article class="abs news" style="top:1802px">
  <div class="thumb" role="img" aria-label="Students in a music rehearsal room"></div>
  <h5>Participation All</h5>
  <p>Randomised words which don't look even slightly believable</p>
  <div class="date">March 28, 2015</div>
</article>
<article class="abs news" style="top:1958px">
  <div class="thumb" role="img" aria-label="Students attending a class session"></div>
  <h5>Participation All</h5>
  <p>Randomised words which don't look even slightly believable</p>
  <div class="date">March 28, 2015</div>
</article>

<div class="abs map" role="img" aria-label="Street map showing the location of Larchmere Valley College"></div>

<footer>
  <div class="abs footer"></div>
  <div class="abs foot-col foot-about" style="left:172px;width:258px">
    <h6>ABOUT INVENT</h6>
    <p>There are many variations of passages of Lorem Ipsum available, but the majority have suffered alteration in some form, by injected t use a passage</p>
  </div>
  <div class="abs foot-col" style="left:470px;width:258px">
    <h6>Recent Post</h6>
    <div class="post">
      <div class="thumb" role="img" aria-label="Students working at a table"></div>
      <div><b>School of Technology</b><span>September 23, 2014</span></div>
    </div>
  </div>
  <div class="abs foot-col" style="left:767px;width:261px">
    <h6>FIND US ONLINE</h6>
    <div class="social">
      <div><i></i>Friendsphere</div>
      <div><i></i>Chirper</div>
      <div><i></i>Searchplus</div>
      <div><i></i>Snapframe</div>
    </div>
  </div>
  <div class="abs bottom">
    <span style="left:172px">Copyrights@Larchmere Valley College.2014</span>
    <span style="left:690px;width:338px;text-align:right">1820 Alder Ridge Road • PO Box 412 • Kestrel Falls</span>
  </div>
</footer>

</body>
</html>
```